Business Card design for new private practice opening

I need a business card design for my new private practice with my new logo uploaded as a file
On the front the logo
On the back: maybe a small logo somewhere?
Priv. Doz. DDr. Corinna Vestaluk
Fachärztin für Allgemein- & Viszeralchirurgie
Address: xxx
Tel: xxx
Mobil:xxx
Webseite:xxx
Email:xxx

Contact Information for Business Card

See project description above for details

Requirements
Nice to have
• I would like the colors of the logo incorporated into the business card

```html
<!DOCTYPE html>
<html lang="de">
<head>
<meta charset="utf-8">
<title>Vestaluk Chirurgie – Visitenkarte</title>
<link href="https://fonts.googleapis.com/css2?family=Montserrat:wght@400;500;600;700&display=swap" rel="stylesheet">
<style>
  :root {
    --teal: #45b8b5;
    --teal-light: #52c0bd;
    --teal-dark: #3aa9a6;
    --grey-text: #6e6e6e;
    --ink: #222222;
    --rule: #8a8a8a;
    --stripe: #8d8d8d;
    --paper: #ffffff;
    --backdrop: #e6e7e8;
  }
  * { box-sizing: border-box; margin: 0; padding: 0; }
  html, body {
    width: 1200px; height: 1200px; overflow: hidden;
    background: var(--backdrop);
    font-family: "Montserrat", sans-serif;
  }
  .sheet {
    position: relative; width: 1200px; height: 1200px;
  }
  .card {
    position: absolute; left: 120px; width: 960px; height: 548px;
    border-radius: 44px; overflow: hidden;
    box-shadow: 0 10px 30px rgba(0,0,0,0.18);
  }
  .card--front { top: 36px; background: var(--paper); }
  .card--back {
    top: 616px;
    background: linear-gradient(160deg, var(--teal-light), var(--teal-dark));
  }

  .brand { position: absolute; display: flex; align-items: center; }
  .brand__dot { border-radius: 50%; flex: none; }
  .brand__name { font-weight: 700; text-transform: uppercase; letter-spacing: 0.04em; line-height: 1.02; }

  .card--front .brand { left: 410px; top: 62px; gap: 22px; }
  .card--front .brand__dot { width: 92px; height: 92px; background: var(--teal); border: 5px solid #7c7c7c; }
  .card--front .brand__name { color: var(--grey-text); font-size: 42px; }

  .wave { position: absolute; inset: 0; width: 960px; height: 548px; }

  .person { position: absolute; left: 44px; top: 318px; width: 520px; }
  .person__name { color: var(--teal); font-size: 27px; font-weight: 600; text-transform: uppercase; letter-spacing: 0.01em; white-space: nowrap; }
  .person__title { color: var(--ink); font-size: 13.5px; font-weight: 500; text-transform: uppercase; margin-top: 4px; letter-spacing: 0.02em; }
  .rule { height: 1.5px; background: var(--rule); }
  .person .rule { margin-top: 14px; width: 500px; }

  .contact { list-style: none; }
  .contact__item { display: flex; align-items: center; gap: 16px; color: var(--ink); font-size: 27px; font-weight: 400; }
  .contact__item svg { flex: none; }
  .person .contact { margin-top: 14px; }
  .person .contact__item + .contact__item { margin-top: 6px; }

  .location { position: absolute; left: 620px; top: 262px; width: 300px; }
  .location .contact { margin-top: 16px; }
  .location .contact__item { font-size: 23px; align-items: flex-start; line-height: 1.2; }

  .website { position: absolute; right: 48px; top: 434px; color: #ffffff; font-size: 24px; font-weight: 500; letter-spacing: 0.05em; }

  .card--back .brand { left: 210px; top: 150px; gap: 38px; }
  .card--back .brand__dot { width: 200px; height: 200px; border: 8px solid #ffffff; }
  .card--back .brand__name { color: #ffffff; font-size: 76px; }
</style>
</head>
<body>
<main class="sheet">

  <section class="card card--front" aria-label="Vorderseite">
    <svg class="wave" viewBox="0 0 960 548" aria-hidden="true">
      <path d="M0,500 L540,500 C610,500 620,386 690,380 L960,380 L960,548 L0,548 Z" fill="var(--stripe)"/>
      <path d="M0,512 L560,512 C630,512 640,396 712,392 L960,392 L960,548 L0,548 Z" fill="var(--teal)"/>
    </svg>

    <div class="brand">
      <span class="brand__dot"></span>
      <span class="brand__name">Vestaluk<br>Chirurgie</span>
    </div>

    <div class="person">
      <p class="person__name">Priv. Doz. DDr. Corinna Vestaluk</p>
      <p class="person__title">Fachärztin für Allgemein- &amp; Viszeralchirurgie</p>
      <div class="rule"></div>
      <ul class="contact">
        <li class="contact__item">
          <svg width="28" height="28" viewBox="0 0 24 24" aria-hidden="true"><path fill="var(--teal)" d="M6.6 10.8a15.1 15.1 0 0 0 6.6 6.6l2.2-2.2c.3-.3.7-.4 1-.2 1.1.4 2.3.6 3.6.6.6 0 1 .4 1 1V20c0 .6-.4 1-1 1A17 17 0 0 1 3 4c0-.6.4-1 1-1h3.5c.6 0 1 .4 1 1 0 1.3.2 2.5.6 3.6.1.3 0 .7-.2 1z"/></svg>
          (000) 000 0000
        </li>
        <li class="contact__item">
          <svg width="28" height="22" viewBox="0 0 28 22" aria-hidden="true"><rect width="28" height="22" rx="2" fill="var(--teal)"/><path d="M2 3 L14 12 L26 3" fill="none" stroke="#fff" stroke-width="2.2"/></svg>
          email@company.com
        </li>
      </ul>
    </div>

    <div class="location">
      <div class="rule"></div>
      <ul class="contact">
        <li class="contact__item">
          <svg width="22" height="30" viewBox="0 0 22 30" aria-hidden="true"><path d="M11 1C5.5 1 1 5.3 1 10.8 1 18 11 29 11 29s10-11 10-18.2C21 5.3 16.5 1 11 1z" fill="none" stroke="var(--teal)" stroke-width="3"/><circle cx="11" cy="11" r="3.5" fill="var(--teal)"/></svg>
          <span>123 Name Street, 000<br>Your City, 00000-000</span>
        </li>
      </ul>
    </div>

    <p class="website">www.company.com</p>
  </section>

  <section class="card card--back" aria-label="Rückseite">
    <div class="brand">
      <span class="brand__dot"></span>
      <span class="brand__name">Vestaluk<br>Chirurgie</span>
    </div>
  </section>

</main>
</body>
</html>
```